Für ein Ebook mit dem Titel 'Lichtung - Atemzug für das Herz' mit dem Autorennamen Corinna Wendel benötige ich ein ansprechendes Cover.
Es sollte nicht zu bunt sein. Eher sinnlich und beruhigend. Erdtöne

```html
<!DOCTYPE html>
<html lang="de">
<head>
<meta charset="utf-8">
<title>Lichtung – Atemzug für das Herz · Corinna Wendel</title>
<link rel="stylesheet" href="https://fonts.googleapis.com/css2?family=Catamaran:wght@400;700&family=Yellowtail&display=swap">
<style>
  :root {
    --sky-light: #f0d27e;
    --sky-mid: #c9a456;
    --sky-haze: #b8924f;
    --dune-gold: #a9782e;
    --dune-mid: #6e3f1a;
    --dune-deep: #3a1a0f;
    --dune-night: #2a120b;
    --author-ink: #1e1510;
    --title-gold: #f6df82;
    --subtitle-cream: #fffbd2;
    --rule-light: rgba(255, 236, 190, 0.55);
  }
  html, body {
    margin: 0;
    padding: 0;
    width: 750px;
    height: 1200px;
    overflow: hidden;
    background: var(--dune-night);
  }
  .cover {
    position: relative;
    width: 750px;
    height: 1200px;
    overflow: hidden;
  }
  .cover__backdrop {
    position: absolute;
    inset: 0;
    background:
      radial-gradient(circle at 96px 196px, rgba(255,255,240,0.95) 0, rgba(255,240,180,0.6) 30px, rgba(240,210,126,0) 180px),
      linear-gradient(180deg,
        var(--sky-haze) 0%,
        var(--sky-light) 20%,
        var(--sky-mid) 34%,
        var(--dune-gold) 42%,
        #8a5a24 50%,
        #b3842f 58%,
        var(--dune-mid) 70%,
        var(--dune-deep) 85%,
        var(--dune-night) 100%);
  }
  .cover__author {
    position: absolute;
    top: 52px;
    left: 0;
    right: 0;
    margin: 0;
    text-align: center;
    font-family: "Catamaran", sans-serif;
    font-weight: 700;
    font-size: 62px;
    line-height: 1;
    color: var(--author-ink);
    letter-spacing: 0.5px;
  }
  .cover__rule {
    position: absolute;
    left: 0;
    width: 750px;
    height: 10px;
    border-top: 1px solid var(--rule-light);
    border-bottom: 1px solid var(--rule-light);
  }
  .cover__rule--top { top: 465px; }
  .cover__rule--bottom { top: 856px; }
  .cover__title {
    position: absolute;
    top: 540px;
    left: 0;
    right: 0;
    margin: 0;
    text-align: center;
  }
  .cover__title-main {
    display: block;
    font-family: "Yellowtail", cursive;
    font-weight: 400;
    font-size: 124px;
    line-height: 1;
    color: var(--title-gold);
  }
  .cover__title-sub {
    display: block;
    margin-top: 4px;
    font-family: "Catamaran", sans-serif;
    font-weight: 400;
    font-size: 66px;
    line-height: 1;
    color: var(--subtitle-cream);
  }
  .cover__title-sub .small {
    font-size: 33px;
  }
</style>
</head>
<body>
  <main class="cover">
    <div class="cover__backdrop" role="img" aria-label="Goldene Wüstendünen unter strahlender Sonne im warmen Dunst"></div>
    <p class="cover__author">Corinna Wendel</p>
    <div class="cover__rule cover__rule--top"></div>
    <h1 class="cover__title">
      <span class="cover__title-main">Lichtung</span>
      <span class="cover__title-sub">Atemzug <span class="small">für das</span> Herz</span>
    </h1>
    <div class="cover__rule cover__rule--bottom"></div>
  </main>
</body>
</html>
```